I'm looking for strong image and design for the first book in a series titled "Theodore Pellbrook On A Voyage Through Our Convictions" subtitle "Taking Hold of Living"; although it's about beliefs, I'm not look for an ethereal feel as the first book is about how our beliefs impact our actions and expectations. I'm a published philosopher and keen on branding my name for professional purposes hence the use of my name :) The book will initially be an e-book but I will follow up with a paperback soon afterwards. My website http://theodorepellbrook-example.com/ may provide some help on me and my projects. Thanks, Theo

Target Market(s)

Graduates and corporate folk who tend to lose their way in the systems.

Logo Text

Theodore Pellbrook on Convictions

Font styles to use
Sans Serif

Colors

Designer to choose colors to be used in the design.

Requirements
Must have
• Needless to say, but impact.
Nice to have
• Strong colours
Should not have
• Religious imagery; the book is philosophical and leans into living in this world.

```html
<!DOCTYPE html>
<html lang="en">
<head>
<meta charset="utf-8">
<title>On A Voyage Through Our Convictions — Theodore Pellbrook</title>
<link href="https://fonts.googleapis.com/css2?family=Great+Vibes&family=Lato:wght@300;400;700&display=swap" rel="stylesheet">
<style>
  :root {
    --sky-deep: #0f2a4a;
    --sky-teal: #1a8a9c;
    --sky-bright: #2aa9bc;
    --band-violet: #6a4d7e;
    --band-peach: #f3c29a;
    --band-umber: #4a2a2a;
    --sunset-orange: #f0a060;
    --sunset-red: #d84a2a;
    --water-teal: #2b7e94;
    --water-deep: #0b3550;
    --ink-white: #ffffff;
    --script-gold: #f6bd6f;
  }
  html, body {
    margin: 0;
    padding: 0;
    width: 800px;
    height: 1200px;
    overflow: hidden;
    background: var(--sky-deep);
  }
  .cover {
    position: relative;
    width: 800px;
    height: 1200px;
    overflow: hidden;
    font-family: "Lato", sans-serif;
    color: var(--ink-white);
  }
  .cover__scene {
    position: absolute;
    inset: 0;
    background: linear-gradient(to bottom,
      var(--sky-deep) 0%,
      #124e6e 15%,
      var(--sky-teal) 30%,
      var(--sky-bright) 36%,
      #3b6d9a 39%,
      var(--band-violet) 41%,
      #d89a6a 43%,
      var(--band-peach) 45%,
      var(--band-umber) 47%,
      #8a5a3a 49%,
      var(--sunset-orange) 52%,
      var(--sunset-red) 55%,
      #c2562e 59%,
      #8a6a6a 65%,
      var(--water-teal) 72%,
      #1b6a8a 85%,
      var(--water-deep) 100%);
  }
  .cover__tagline {
    position: absolute;
    top: 42px;
    left: 0;
    width: 100%;
    text-align: center;
    font-size: 29px;
    font-weight: 400;
    letter-spacing: 0.22em;
    text-transform: uppercase;
    margin: 0;
  }
  .cover__title {
    margin: 0;
    font-weight: normal;
  }
  .cover__title-lead {
    position: absolute;
    top: 160px;
    left: 370px;
    font-size: 48px;
    font-weight: 300;
    letter-spacing: 0.02em;
  }
  .cover__title-script {
    position: absolute;
    top: 150px;
    left: 0;
    width: 100%;
    text-align: center;
    font-family: "Great Vibes", cursive;
    font-size: 250px;
    line-height: 1;
    color: var(--script-gold);
  }
  .cover__title-tail {
    position: absolute;
    top: 590px;
    left: 0;
    width: 100%;
    text-align: center;
    font-size: 44px;
    font-weight: 400;
    letter-spacing: 0.005em;
  }
  .cover__author {
    position: absolute;
    top: 1082px;
    left: 0;
    width: 100%;
    text-align: center;
    font-size: 56px;
    font-weight: 400;
    letter-spacing: 0.01em;
    margin: 0;
  }
</style>
</head>
<body>
  <main class="cover">
    <div class="cover__scene" role="img" aria-label="Abstract sunset over calm water: deep teal sky, streaks of violet, peach and orange at the horizon, and rippling blue water below"></div>
    <p class="cover__tagline">Taking Hold of Living</p>
    <h1 class="cover__title">
      <span class="cover__title-lead">ON A</span>
      <span class="cover__title-script">Voyage</span>
      <span class="cover__title-tail">THROUGH OUR CONVICTIONS</span>
    </h1>
    <p class="cover__author">THEODORE PELLBROOK</p>
  </main>
</body>
</html>
```